Simple fencing and steel manufacturing website

** update 01/04/2015 ** we did not add logo design, but if your font/logo is accepted we will add $50 to make it more fair
Even if you web design is not chosen, but your logo is, we will pay you $50. If both are chosen you will get an extra $50
Open brief

Site map:
Home
About
Gallery
-photos
-testimonials
Contact

No current website:

No current logo, colors currently black and gold but we don't mind changing them - wide open brief
Happy for new font/style/logo for company name which is Paling Brightway

Customer wants clean, credible and professional look & feel
stock photos OK

Brief:

One home page - simple with 2 or 3 small areas to tease and attract the user and one template page to suit all the other pages

All competitor websites are pretty bad, the best of them is
http://www.wexmoorrailing.com.au/index.html

Target Market(s)

Government and top level builders

Industry/Entity Type

Fencing

Requirements
Must have
• 1. Display ISO and environmental awards (ISO9001 AS4801 ISO14001)
• 2. A list of about 15 products
• Can be in teaser areas of home page as suggested before or slider or really anywhere
Nice to have
• Log with name - nice but not necessary (we don't have one)

```html
<!DOCTYPE html>
<html lang="en">
<head>
<meta charset="utf-8">
<title>Paling Brightway – Fencing &amp; Steel</title>
<link href="https://fonts.googleapis.com/css2?family=Jost:ital,wght@0,400;0,500;0,600;1,400&display=swap" rel="stylesheet">
<style>
  :root{
    --navy:#2f2a5a;
    --orange:#e37517;
    --grey:#6e6c6d;
    --text:#555559;
    --line:#d6d6d6;
    --white:#ffffff;
    --search:#ececec;
  }
  *{box-sizing:border-box;margin:0;padding:0}
  html,body{width:1200px;height:1175px;overflow:hidden;background:var(--white)}
  body{font-family:"Jost",sans-serif;color:var(--text);position:relative}
  a{color:inherit;text-decoration:none}
  .abs{position:absolute}

  /* top bar */
  .topbar{left:0;top:0;width:1200px;height:25px;background:var(--navy)}
  .topnav a{position:absolute;top:0;height:25px;line-height:25px;font-size:11px;color:var(--white);text-transform:uppercase}
  .topnav a.active{background:var(--orange);padding:0 6px}

  /* header */
  .phone{left:148px;top:54px;font-size:21px;letter-spacing:.5px;color:var(--text)}
  .header-bulge{left:464px;top:80px;width:272px;height:61px;background:var(--white);border-radius:0 0 50% 50%/0 0 100% 100%;z-index:2}
  .brand{display:flex;align-items:center;gap:8px;z-index:3}
  .brand-mark{width:44px;height:44px;background:var(--orange)}
  .brand-name{font-weight:600;font-size:23px;line-height:24px;color:var(--navy);letter-spacing:.5px;text-transform:uppercase}
  .search{left:815px;top:56px;width:200px;height:29px;background:var(--search);border-radius:3px;font-size:12px;color:#aaa;padding:8px 10px}
  .search-btn{left:1018px;top:56px;width:32px;height:29px;background:var(--search);border-radius:3px}

  /* hero */
  .hero{left:0;top:111px;width:1200px;height:425px;background:radial-gradient(ellipse at 70% 40%,#6a615c 0%,#4a423e 45%,#2a2523 100%)}
  .hero-title{left:143px;top:190px;font-size:64px;font-weight:500;color:var(--white);letter-spacing:1px;z-index:3}
  .hero-text{left:151px;top:288px;width:390px;font-size:17px;line-height:25px;color:var(--white);z-index:3}
  .hero-btn{left:153px;top:397px;width:332px;height:47px;background:var(--orange);border:2px solid var(--white);border-radius:3px;color:var(--white);font-size:20px;text-align:center;line-height:43px;text-transform:uppercase;z-index:3}
  .thumb{top:469px;width:43px;height:34px;z-index:3}
  .thumb.active{border:2px solid var(--white)}

  /* products */
  .products-tab{left:350px;top:520px;width:473px;height:30px;background:var(--white);border-radius:4px 4px 0 0;z-index:3}
  .products-title{left:350px;top:522px;width:473px;text-align:center;font-size:21px;color:var(--text);text-transform:uppercase;letter-spacing:.5px;z-index:4}
  .rule{left:150px;width:900px;height:1px;background:var(--line)}
  .col-divider{top:557px;width:1px;height:165px;background:var(--line)}
  .product-list{list-style:none;top:578px}
  .product-list li{height:27px;font-size:12px;line-height:18px;color:var(--text);padding-left:12px;position:relative}
  .product-list li::before{content:"»";position:absolute;left:0;top:-1px;font-size:10px;color:#888}

  /* teaser tiles */
  .tile{top:740px;width:291px;height:168px}
  .tile-range{left:151px;background:var(--navy)}
  .tile-advantage{left:455px;background:var(--orange)}
  .tile-location{left:759px;background:var(--grey)}
  .tile-label{position:absolute;left:11px;bottom:14px;font-size:14px;color:var(--white);text-transform:uppercase}
  .tile svg{position:absolute;left:50%;top:58px;transform:translateX(-50%)}

  /* commitment */
  .commitment{left:150px;top:963px;font-size:26px;line-height:38px;font-style:italic;color:var(--text)}
  .cert{top:937px;width:69px;height:135px}
  .cert-head{height:18px;background:#d9d9d9}
  .cert-body{height:92px;margin-top:4px}
  .cert-foot{height:14px;margin-top:4px;background:#3a3a3a}
  .cert-sub{height:3px;margin-top:1px;background:#9a9a9a}

  .to-top{left:1118px;top:1052px;width:59px;height:40px;background:#8a8a8a;color:var(--white);font-size:11px;font-weight:600;text-align:center;line-height:40px}

  /* footer */
  .social{top:1094px;width:40px;height:40px;border-radius:50%;background:var(--navy)}
  .footer-brand{left:883px;top:1106px}
  .footer-brand .brand-mark{width:44px;height:44px}
  .footer-brand .brand-name{font-size:24px;line-height:24px}
  .copyright{left:152px;top:1150px;font-size:9px;color:var(--text)}
  .footer-nav a{position:absolute;top:1151px;font-size:9px;color:var(--text);text-transform:uppercase}
</style>
</head>
<body>

<nav class="abs topbar topnav" aria-label="Primary">
  <a class="active" href="#" style="left:150px">Home</a>
  <a href="#" style="left:213px">About us</a>
  <a href="#" style="left:289px">Gallery</a>
  <a href="#" style="left:820px">Photos</a>
  <a href="#" style="left:888px">Testimonials</a>
  <a href="#" style="left:982px">Contact</a>
</nav>

<div class="abs phone">(02) 5550 1840</div>
<div class="abs header-bulge"></div>
<div class="abs brand" style="left:509px;top:54px">
  <div class="brand-mark"></div>
  <div class="brand-name">Paling<br>Brightway</div>
</div>
<div class="abs search">Search...</div>
<div class="abs search-btn">
  <svg width="32" height="29" viewBox="0 0 32 29"><circle cx="15" cy="13" r="6" fill="none" stroke="#2f2a5a" stroke-width="2.5"/><line x1="19.5" y1="17.5" x2="24" y2="22" stroke="#2f2a5a" stroke-width="3" stroke-linecap="round"/></svg>
</div>

<section class="abs hero" role="img" aria-label="Close-up photo of rusted steel wire mesh fencing"></section>
<h1 class="abs hero-title">Title goes here</h1>
<p class="abs hero-text">Lorem ipsum dolor sit amet consecutor. Lorem ipsum. Lorem ipsum dolor sit amet consecutor. Lorem ipsum</p>
<a class="abs hero-btn" href="#">View our products</a>

<div class="abs thumb" style="left:764px;background:linear-gradient(#9aa27a,#5f6a3e)" role="img" aria-label="Thumbnail of fence posts"></div>
<div class="abs thumb active" style="left:818px;background:linear-gradient(#5a5350,#2a2523)" role="img" aria-label="Thumbnail of wire mesh"></div>
<div class="abs thumb" style="left:872px;background:linear-gradient(#8fa6c4,#3b3a36)" role="img" aria-label="Thumbnail of steel palisade fence"></div>
<div class="abs thumb" style="left:926px;background:linear-gradient(#7da3d6,#b79b6c)" role="img" aria-label="Thumbnail of sports ground fencing"></div>
<div class="abs thumb" style="left:981px;background:linear-gradient(#a9c6ea,#3a3f55)" role="img" aria-label="Thumbnail of security fence"></div>
<svg class="abs" style="left:1037px;top:476px;z-index:3" width="14" height="20" viewBox="0 0 14 20"><path d="M3 2l8 8-8 8" fill="none" stroke="#fff" stroke-width="3"/></svg>

<div class="abs products-tab"></div>
<h2 class="abs products-title">Our Products</h2>
<div class="abs rule" style="top:557px"></div>
<div class="abs col-divider" style="left:416px"></div>
<div class="abs col-divider" style="left:778px"></div>
<ul class="abs product-list" style="left:153px">
  <li>Product Link 1</li><li>Product Link 2</li><li>Product Link 3</li><li>Product Link 4</li><li>Product Link 5</li>
</ul>
<ul class="abs product-list" style="left:435px">
  <li>Product Link 1</li><li>Product Link 2</li><li>Product Link 3</li><li>Product Link 4</li><li>Product Link 5</li>
</ul>
<ul class="abs product-list" style="left:796px">
  <li>Product Link 1</li><li>Product Link 2</li><li>Product Link 3</li><li>Product Link 4</li><li>Product Link 5</li>
</ul>
<div class="abs rule" style="top:721px"></div>

<a class="abs tile tile-range" href="#">
  <svg width="66" height="50" viewBox="0 0 66 50"><rect x="0" y="0" width="30" height="16" fill="#fff"/><rect x="38" y="0" width="28" height="16" fill="#fff"/><rect x="0" y="22" width="30" height="26" fill="#fff"/><rect x="39.5" y="29.5" width="25" height="17" fill="none" stroke="#fff" stroke-width="3"/><rect x="3" y="3" width="24" height="10" fill="none" stroke="#2f2a5a" stroke-width="3"/></svg>
  <span class="tile-label">Our range</span>
</a>
<a class="abs tile tile-advantage" href="#">
  <svg width="68" height="52" viewBox="0 0 68 52"><path d="M0 6l12-4 12 6-8 10 6 4 10-8 12 10-14 14-10 6-8-6-6-6L0 22z" fill="#fff"/><path d="M68 4l-12-2-16 6-10 10 6 4 12-8 12 12 8-6z" fill="#fff"/><circle cx="20" cy="40" r="3" fill="#fff"/><circle cx="26" cy="45" r="3" fill="#fff"/></svg>
  <span class="tile-label">Our advantage</span>
</a>
<a class="abs tile tile-location" href="#">
  <svg width="44" height="62" viewBox="0 0 44 62"><path d="M22 0C10 0 0 10 0 22c0 14 22 40 22 40s22-26 22-40C44 10 34 0 22 0z" fill="#fff"/><circle cx="22" cy="21" r="9" fill="#6e6c6d"/></svg>
  <span class="tile-label">Location</span>
</a>

<div class="abs rule" style="top:927px"></div>
<p class="abs commitment">Our commitment to Quality, Environmental<br>and OHS standards is your guarantee.</p>

<div class="abs cert" style="left:721px" role="img" aria-label="Quality management certification badge">
  <div class="cert-head"></div><div class="cert-body" style="background:#e0203a"></div><div class="cert-foot"></div><div class="cert-sub"></div>
</div>
<div class="abs cert" style="left:854px" role="img" aria-label="Environmental management certification badge">
  <div class="cert-head"></div><div class="cert-body" style="background:#1f8d3b"></div><div class="cert-foot"></div><div class="cert-sub"></div>
</div>
<div class="abs cert" style="left:980px" role="img" aria-label="Occupational health and safety certification badge">
  <div class="cert-head"></div><div class="cert-body" style="background:#f6b51c"></div><div class="cert-foot"></div><div class="cert-sub"></div>
</div>

<a class="abs to-top" href="#">TO TOP</a>

<div class="abs rule" style="top:1080px"></div>
<a class="abs social" href="#" style="left:150px" aria-label="Social profile 1"></a>
<a class="abs social" href="#" style="left:197px" aria-label="Social profile 2"></a>
<a class="abs social" href="#" style="left:245px" aria-label="Social profile 3"></a>
<a class="abs social" href="#" style="left:290px" aria-label="Social profile 4"></a>

<div class="abs brand footer-brand">
  <div class="brand-mark"></div>
  <div class="brand-name">Paling<br>Brightway</div>
</div>

<div class="abs copyright">© 2015 Paling Brightway</div>
<nav class="footer-nav" aria-label="Footer">
  <a href="#" style="left:267px">Home</a>
  <a href="#" style="left:320px">About us</a>
  <a href="#" style="left:389px">Gallery</a>
  <a href="#" style="left:452px">Photos</a>
  <a href="#" style="left:514px">Testimonials</a>
  <a href="#" style="left:601px">Contact</a>
</nav>

</body>
</html>
```